Business card design for sports medicine and athlete care clinic.

We need a bold, solid business card design for our practitioners to stand out. We treat overuse & sports-related injuries and provide post-operative rehabilitation. Our specialisations include chronic conditions, men’s health, nutrition & musculoskeletal disorders (MSDs). All brand collateral in terms of fonts, logo and colour palette to be provided.

Target Market(s)

Athletes (professional and amateur), sportspeople, predominantly male

Industry/Entity Type

Health And Wellness

Contact Information for Business Card

The front of the card should be white with dark blue text the back dark blue with white text. The logo should be top-left. The business name should be horizontal and right of the logo. The tagline should be directly below centred on the back of the card (see top-banner.png and bottom-banner.png)

Font styles to use
Sans Serif

Colors
0355a3
0293ce
3176b5
ffffff
85acd3

Requirements
Nice to have
• Diagonal and/or horizontal line elements between logo and practitioner details and/or bottom corner of card (see slide.png and tag-bg.png).

```html
<!DOCTYPE html>
<html lang="en">
<head>
<meta charset="utf-8">
<title>Peak Motion Clinic – Business Card</title>
<link rel="stylesheet" href="https://fonts.googleapis.com/css2?family=Poppins:wght@700&family=Lexend:wght@400;600&display=swap">
<style>
  :root {
    --navy: #1f1f55;
    --blue: #0293ce;
    --mid-blue: #3176b5;
    --light-blue: #85acd3;
    --white: #ffffff;
    --backdrop: #c9c9c9;
    --rule: #1f1f55;
  }
  * { box-sizing: border-box; margin: 0; padding: 0; }
  html, body { width: 1200px; height: 852px; overflow: hidden; }
  body {
    background: var(--backdrop);
    font-family: "Lexend", sans-serif;
    position: relative;
  }
  .card {
    position: absolute;
    top: 276px;
    width: 520px;
    height: 300px;
    border-radius: 22px;
    overflow: hidden;
  }
  /* Back of card */
  .card--back { left: 50px; background: var(--navy); color: var(--white); }
  .back-brand {
    position: absolute; left: 110px; top: 104px;
    display: flex; align-items: center; gap: 16px;
  }
  .brand-mark {
    width: 62px; height: 62px; border-radius: 50%;
    background: linear-gradient(135deg, var(--light-blue), var(--blue));
    flex: none;
  }
  .brand-name {
    font-family: "Poppins", sans-serif; font-weight: 700;
    font-size: 27px; letter-spacing: 0.2px; white-space: nowrap;
  }
  .back-tagline {
    position: absolute; left: 0; right: 0; bottom: 40px;
    text-align: center; font-size: 12px; letter-spacing: 0.3px;
  }
  /* Front of card */
  .card--front { left: 630px; background: var(--white); color: var(--navy); }
  .front-brand { position: absolute; left: 22px; top: 64px; display: flex; gap: 14px; }
  .front-brand .brand-mark { width: 58px; height: 58px; }
  .front-brand .brand-name { font-size: 24px; color: var(--navy); line-height: 1.1; }
  .front-tagline { font-size: 13.5px; color: var(--blue); margin-top: 3px; }
  .practitioner {
    position: absolute; right: 22px; top: 50px; text-align: right;
  }
  .practitioner-name { font-weight: 600; font-size: 15px; }
  .practitioner-role { font-size: 11.5px; color: var(--blue); margin-top: 1px; }
  .header-rule {
    position: absolute; left: 94px; right: 22px; top: 128px;
    height: 1px; background: var(--rule);
  }
  .address {
    position: absolute; right: 22px; top: 136px;
    text-align: right; font-size: 11.5px; line-height: 1.45;
  }
  .contact-rule {
    position: absolute; left: 22px; top: 204px; width: 170px;
    height: 1px; background: var(--rule);
  }
  .contacts {
    position: absolute; left: 22px; top: 212px; list-style: none;
    font-size: 12px; line-height: 1;
  }
  .contacts li { display: flex; align-items: center; gap: 7px; margin-bottom: 6px; }
  .contact-icon { width: 14px; height: 14px; flex: none; }
  .footer-tab { position: absolute; left: 0; top: 0; width: 520px; height: 300px; }
  .footer-links {
    position: absolute; right: 18px; bottom: 14px;
    display: flex; align-items: center; gap: 8px;
    color: var(--white); font-size: 11.5px; white-space: nowrap;
  }
  .social-dot { width: 9px; height: 9px; border-radius: 50%; background: var(--white); }
  .globe-icon { width: 11px; height: 11px; }
</style>
</head>
<body>

<section class="card card--back" aria-label="Back of business card">
  <div class="back-brand">
    <span class="brand-mark" aria-hidden="true"></span>
    <span class="brand-name">Peak Motion Clinic</span>
  </div>
  <p class="back-tagline">Sports medicine and athlete care</p>
</section>

<section class="card card--front" aria-label="Front of business card">
  <svg class="footer-tab" viewBox="0 0 520 300" aria-hidden="true">
    <polygon points="258,248 520,248 520,300 214,300" fill="var(--navy)"/>
  </svg>

  <div class="front-brand">
    <span class="brand-mark" aria-hidden="true"></span>
    <div>
      <div class="brand-name">Peak Motion Clinic</div>
      <div class="front-tagline">Sports medicine and athlete care</div>
    </div>
  </div>

  <div class="practitioner">
    <div class="practitioner-name">Mark Ellison</div>
    <div class="practitioner-role">Managing Director</div>
  </div>
  <div class="header-rule"></div>
  <address class="address" style="font-style:normal">
    118 Harbor Street<br>Suite 210, Fairview<br>MI 49020
  </address>

  <div class="contact-rule"></div>
  <ul class="contacts">
    <li>
      <svg class="contact-icon" viewBox="0 0 14 14" aria-hidden="true">
        <circle cx="7" cy="7" r="7" fill="var(--mid-blue)"/>
        <rect x="4.6" y="3" width="4.8" height="8" rx="1" fill="none" stroke="var(--white)" stroke-width="1.1"/>
      </svg>214-555-0182
    </li>
    <li>
      <svg class="contact-icon" viewBox="0 0 14 14" aria-hidden="true">
        <circle cx="7" cy="7" r="7" fill="var(--mid-blue)"/>
        <path d="M4.3 4.2c.3-.4.8-.4 1 0l.7 1.2c.2.3.1.6-.1.8l-.4.4c.4.9 1 1.5 1.9 1.9l.4-.4c.2-.2.5-.3.8-.1l1.2.7c.4.2.4.7 0 1l-.6.6c-2.5.2-5.6-2.9-5.4-5.4z" fill="var(--white)"/>
      </svg>214-555-0182
    </li>
    <li>
      <svg class="contact-icon" viewBox="0 0 14 14" aria-hidden="true">
        <circle cx="7" cy="7" r="7" fill="var(--mid-blue)"/>
        <rect x="3.5" y="4.5" width="7" height="5" fill="none" stroke="var(--white)" stroke-width="1"/>
        <path d="M3.5 4.7 7 7.4l3.5-2.7" fill="none" stroke="var(--white)" stroke-width="1"/>
      </svg>mark@peakmotionclinic.com
    </li>
  </ul>

  <div class="footer-links">
    <span class="social-dot" aria-hidden="true"></span>
    <span>PeakMotionAU</span>
    <svg class="globe-icon" viewBox="0 0 12 12" aria-hidden="true">
      <circle cx="6" cy="6" r="5.3" fill="none" stroke="var(--white)" stroke-width="1"/>
      <ellipse cx="6" cy="6" rx="2.3" ry="5.3" fill="none" stroke="var(--white)" stroke-width="0.9"/>
      <line x1="0.7" y1="6" x2="11.3" y2="6" stroke="var(--white)" stroke-width="0.9"/>
    </svg>
    <span>peakmotionclinic.com.au</span>
  </div>
</section>

</body>
</html>
```